Clone http://www.velvorquillset.com/ (fully functioning WordPress website - not just design)

1) Clone or recreate http://www.velvorquillset.com/ in Wordpress with WooCommerece plugin
2) Connect to our Existing Quenz Account
3) Make site-wide text only changes that we provide you when site is complete.

We will provide all the graphics according to your size requirements.

Cash awarded to the closest copy of http://www.velvorquillset.com/

Target Market(s)

WordPress developer

Number of Pages Required

5+ page

Font styles to use
Sans Serif

Colors
abd037
cadf82
eaf2ce

Requirements
Must have
• Fully functioning website.

```html
<!DOCTYPE html>
<html lang="en">
<head>
<meta charset="utf-8">
<title>Quenz – Mail Merge Online</title>
<link href="https://fonts.googleapis.com/css2?family=Roboto:wght@300;400;500;700&display=swap" rel="stylesheet">
<style>
:root{
  --green-dark:#3f7d1c;
  --green:#5a9d2c;
  --green-mid:#6aab34;
  --green-light:#8cc63f;
  --lime:#abd037;
  --lime-soft:#cadf82;
  --lime-pale:#eaf2ce;
  --grey-band:#efefef;
  --panel:#e6e6e6;
  --text:#555;
  --text-soft:#777;
  --footer:#474747;
  --footer-dark:#363636;
  --white:#fff;
}
*{box-sizing:border-box;margin:0;padding:0}
html,body{width:1200px;height:2203px;overflow:hidden}
body{position:relative;font-family:'Roboto',Arial,sans-serif;color:var(--text);background:var(--white)}
.abs{position:absolute}
/* top bar */
.topbar{left:0;top:0;width:1200px;height:28px;background:var(--green-dark)}
.follow{left:161px;top:8px;font-size:10px;font-weight:700;color:var(--white);letter-spacing:.3px}
.social-dot{width:18px;height:18px;border-radius:50%;background:var(--green-light);top:5px}
.flag{left:828px;top:5px;width:32px;height:18px;background:linear-gradient(#c8363c 0 50%,#f4f4f4 50% 100%)}
.flag::before{content:"";position:absolute;left:0;top:0;width:14px;height:10px;background:#2e4a8f}
.btn-top{top:0;height:28px;font-size:9px;font-weight:500;color:var(--white);display:flex;align-items:center;justify-content:center;gap:6px;letter-spacing:.3px}
.btn-login{left:867px;width:86px;background:var(--green-mid)}
.btn-register{left:955px;width:85px;background:var(--green-light)}
/* header */
.header{left:0;top:28px;width:1200px;height:85px;background:var(--white);border-bottom:1px solid #e4e4e4}
.brand{left:161px;top:50px;display:flex;align-items:center;gap:10px;font-size:26px;font-weight:700;color:var(--green)}
.brand-dot{width:22px;height:22px;border-radius:50%;background:var(--green)}
.nav{top:64px;font-size:10.5px;color:#666;letter-spacing:.2px}
.nav.active{color:var(--green);font-weight:500}
.nav-underline{left:740px;top:82px;width:31px;height:2px;background:var(--green)}
/* hero */
.hero{left:0;top:113px;width:1200px;height:514px;background:var(--green)}
.hero-visual{left:390px;top:220px;width:734px;height:407px;background:radial-gradient(ellipse at 50% 55%,#8d948f 0 28%,#5f8a43 55%,var(--green) 75%);opacity:.85}
.hero-sub{left:159px;top:255px;font-size:28px;font-weight:400;color:var(--white)}
.hero-title{left:159px;top:290px;font-size:41px;font-weight:700;color:var(--white)}
.hero-text{left:161px;top:352px;width:360px;font-size:17.5px;line-height:21px;color:#eef6e4;font-weight:300}
.btn-outline{border:2px solid var(--white);color:var(--white);font-size:12px;font-weight:700;display:flex;align-items:center;justify-content:center}
.hero-btn{left:161px;top:423px;width:152px;height:41px}
/* intro band */
.intro{left:0;top:627px;width:1200px;height:110px;background:var(--grey-band);text-align:center}
.intro h2{margin-top:25px;font-size:17.5px;font-weight:500;color:var(--green-dark)}
.intro p{width:640px;margin:7px auto 0;font-size:12.5px;line-height:15px;color:var(--text-soft)}
.section-title{left:0;top:782px;width:1200px;text-align:center;font-size:28px;font-weight:300;color:#666}
/* steps */
.step-img{width:600px;height:309px}
.step-panel{width:600px;height:309px;background:var(--panel)}
.step-num{width:60px;height:60px;border:3px solid var(--green-dark);border-radius:50%;font-size:29px;font-weight:500;color:var(--green-dark);display:flex;align-items:center;justify-content:center}
.step-title{font-size:29px;font-weight:300;color:var(--green);letter-spacing:.3px}
.step-sub{font-size:17px;color:#666;font-weight:400}
.step-body{width:345px;font-size:11.2px;line-height:20.3px;color:var(--text-soft)}
/* cta */
.cta{left:0;top:1839px;width:1200px;height:122px;background:linear-gradient(90deg,#8bbd3d,var(--lime) 45%,#9cc83b)}
.cta-text{left:241px;top:1893px;font-size:18px;color:var(--white);font-weight:400}
.cta-btn{left:705px;top:1882px;width:182px;height:41px}
/* footer */
.footer{left:0;top:1961px;width:1200px;height:198px;background:var(--footer)}
.foot-h{top:1980px;font-size:11.5px;font-weight:700;color:#ddd;padding-bottom:3px;border-bottom:1px solid #999}
.foot-brand{left:161px;top:2018px;display:flex;align-items:center;gap:8px;font-size:20px;font-weight:700;color:#ddd}
.foot-brand span{width:14px;height:14px;border-radius:50%;background:#ddd}
.foot-about{left:161px;top:2085px;width:280px;font-size:10.5px;line-height:12.5px;color:#bbb}
.foot-link{font-size:10.5px;color:#ccc}
.foot-link::before{content:"›";margin-right:14px;color:#aaa}
.foot-icon{left:762px;width:22px;height:22px;border:1px solid #aaa;border-radius:50%}
.foot-contact{left:806px;font-size:10.5px;line-height:14px;color:#ccc}
.foot-social{top:2118px;width:20px;height:20px;border-radius:50%;background:#888}
.copyright{left:0;top:2159px;width:1200px;height:44px;background:var(--footer-dark);text-align:center;font-size:9.5px;color:#bbb;line-height:44px}
</style>
</head>
<body>
<!-- top bar -->
<div class="abs topbar"></div>
<div class="abs follow">FOLLOW US ON:</div>
<div class="abs social-dot" style="left:254px"></div>
<div class="abs social-dot" style="left:278px"></div>
<div class="abs social-dot" style="left:302px"></div>
<div class="abs flag" role="img" aria-label="Language flag"></div>
<div class="abs btn-top btn-login">
  <svg width="9" height="10" viewBox="0 0 9 10"><rect x="0" y="4" width="9" height="6" fill="#fff"/><path d="M2 4V3a2.5 2.5 0 0 1 5 0v1" stroke="#fff" fill="none" stroke-width="1.4"/></svg>LOGIN</div>
<div class="abs btn-top btn-register">
  <svg width="11" height="10" viewBox="0 0 11 10"><circle cx="4" cy="3" r="2.5" fill="#fff"/><path d="M0 10a4 4 0 0 1 8 0z" fill="#fff"/><path d="M9 3v4M7 5h4" stroke="#fff" stroke-width="1.2"/></svg>REGISTER</div>

<!-- header -->
<div class="abs header"></div>
<div class="abs brand"><span class="brand-dot"></span>Quenz</div>
<div class="abs nav active" style="left:740px">HOME</div>
<div class="abs nav-underline"></div>
<div class="abs nav" style="left:795px">TOUR
  <svg width="8" height="6" viewBox="0 0 8 6" style="margin-left:4px"><path d="M1 1l3 3 3-3" stroke="#666" fill="none"/></svg></div>
<div class="abs nav" style="left:856px">PRICE</div>
<div class="abs nav" style="left:906px">OUR TEAM</div>
<div class="abs nav" style="left:980px">CONTACT US</div>

<!-- hero -->
<section class="abs hero"></section>
<div class="abs hero-visual" role="img" aria-label="Desk scene with open laptop, notebook, pen, plant and a hand holding a coffee cup"></div>
<div class="abs hero-sub">LOREM IPSUM DOLOR SIT</div>
<h1 class="abs hero-title">FUSCE BIBENDUM</h1>
<p class="abs hero-text">Pellentesque dolor tortor, lacinia in arcu eu, consectetur varius magna.</p>
<a class="abs btn-outline hero-btn">START A FREE TRAIL</a>

<!-- intro -->
<section class="abs intro">
  <h2>Maecenas facilisis tristique eleifend. Proin in viverra leo, eu lobortis nibh?</h2>
  <p>Fusce bibendum luctus orci, eu consectetur nisi pharetra quis. Fusce condimentum metus nec dui aliquet facilisis sit amet eu nibh. Nunc dolor libero, gravida id enim ac, dictum imperdiet neque.</p>
</section>
<h2 class="abs section-title">100% EASIER THAN USING SCRIBEWRIGHT DOCS!</h2>

<!-- step 1 -->
<div class="abs step-img" style="left:0;top:855px;background:radial-gradient(ellipse at 45% 50%,#f4efe6 0 30%,#e8bd62 65%)" role="img" aria-label="Stationery mockup with letterhead, business cards and tape on a yellow surface"></div>
<div class="abs step-panel" style="left:600px;top:855px"></div>
<div class="abs step-num" style="left:620px;top:892px">1</div>
<div class="abs step-title" style="left:695px;top:904px">UPLOAD YOUR DATA</div>
<div class="abs step-sub" style="left:695px;top:966px">Pellentesque dolor tortor, lacinia in arcu eu</div>
<p class="abs step-body" style="left:695px;top:1000px">Lorem ipsum dolor sit amet, consectetur adipiscing elit. Nullam varius, mi ut rutrum mollis, justo ante imperdiet massa, eu tincidunt velit leo eget quam. Aliquam erat volutpat. Pellentesque faucibus facilisis augue nec aliquam. Fusce aliquet at lorem eu viverra. Orci varius natoque penatibus et magnis dis parturient montes, nascetur ridiculus mus. Etiam suscipit magna vel est aliquam, feugiat placerat velit elementum.</p>

<!-- step 2 -->
<div class="abs step-panel" style="left:0;top:1163px"></div>
<div class="abs step-num" style="left:161px;top:1203px">2</div>
<div class="abs step-title" style="left:236px;top:1215px">DESIGN YOUR TEMPLATE</div>
<div class="abs step-sub" style="left:238px;top:1278px">Vestibulum laoreet purus ut lorem blandit</div>
<p class="abs step-body" style="left:238px;top:1311px;width:340px">Lorem ipsum dolor sit amet, consectetur adipiscing elit. Nullam varius, mi ut rutrum mollis, justo ante imperdiet massa, eu tincidunt velit leo eget quam. Aliquam erat volutpat. Pellentesque faucibus facilisis augue nec aliquam. Fusce aliquet at lorem eu viverra. Orci varius natoque penatibus et magnis dis parturient montes, nascetur ridiculus mus. Etiam suscipit magna vel est aliquam, feugiat placerat velit elementum.</p>
<div class="abs step-img" style="left:600px;top:1163px;background:radial-gradient(ellipse at 55% 50%,#4a3d5e 0 18%,#a6dbe0 45%,#7cc6cf 90%)" role="img" aria-label="Tablet mockup floating over a pale teal background"></div>

<!-- step 3 -->
<div class="abs step-img" style="left:0;top:1472px;background:radial-gradient(ellipse at 40% 45%,#f2f2f2 0 30%,#2a4fae 55%)" role="img" aria-label="Paper sheet mockup with yellow lettering on a blue background"></div>
<div class="abs step-panel" style="left:600px;top:1472px"></div>
<div class="abs step-num" style="left:620px;top:1514px">3</div>
<div class="abs step-title" style="left:695px;top:1526px">MERGE TO PDF</div>
<div class="abs step-sub" style="left:695px;top:1590px">Maecenas facilisis tristique eleifend</div>
<p class="abs step-body" style="left:695px;top:1623px">Lorem ipsum dolor sit amet, consectetur adipiscing elit. Nullam varius, mi ut rutrum mollis, justo ante imperdiet massa, eu tincidunt velit leo eget quam. Aliquam erat volutpat. Pellentesque faucibus facilisis augue nec aliquam. Fusce aliquet at lorem eu viverra. Orci varius natoque penatibus et magnis dis parturient montes, nascetur ridiculus mus. Etiam suscipit magna vel est aliquam, feugiat placerat velit elementum.</p>

<!-- call to action -->
<section class="abs cta" role="img" aria-label="Faint green-toned desk photo behind the call to action"></section>
<div class="abs cta-text">START BUILDING YOUR MAIL MERGE ONLINE NOW!</div>
<a class="abs btn-outline cta-btn">START A FREE TRAIL NOW</a>

<!-- footer -->
<footer class="abs footer"></footer>
<div class="abs foot-h" style="left:161px">ABOUT US</div>
<div class="abs foot-h" style="left:463px">QUICK LINKS</div>
<div class="abs foot-h" style="left:762px">GET IN TOUCH</div>
<div class="abs foot-brand"><span></span>Quenz</div>
<p class="abs foot-about">Lorem ipsum dolor sit amet, consectetur adipiscing elit. Nullam varius, mi ut rutrum mollis, justo ante imperdiet massa, eu tincidunt velit leo eget quam. Aliquam erat volutpat. Pellentesque faucibus facilisis augue nec aliquam.</p>
<div class="abs foot-link" style="left:463px;top:2024px">Home</div>
<div class="abs foot-link" style="left:463px;top:2050px">About us</div>
<div class="abs foot-link" style="left:463px;top:2075px">Team</div>
<div class="abs foot-link" style="left:463px;top:2101px">Tour</div>
<div class="abs foot-link" style="left:463px;top:2126px">Price</div>
<div class="abs foot-link" style="left:593px;top:2024px">Privacy Policy</div>
<div class="abs foot-link" style="left:593px;top:2050px">Terms &amp; Conditions</div>
<div class="abs foot-link" style="left:593px;top:2075px">Refund Policy</div>
<div class="abs foot-icon" style="top:2025px">
  <svg width="20" height="20" viewBox="0 0 20 20"><path d="M10 5a3 3 0 0 1 3 3c0 2.5-3 6-3 6s-3-3.5-3-6a3 3 0 0 1 3-3z" fill="none" stroke="#ccc"/><circle cx="10" cy="8" r="1" fill="#ccc"/></svg></div>
<div class="abs foot-contact" style="top:2023px">demo address #8901<br>de Finibus Bonorum et Malorum</div>
<div class="abs foot-icon" style="top:2066px">
  <svg width="20" height="20" viewBox="0 0 20 20"><rect x="6" y="7" width="8" height="6" fill="#ccc"/><path d="M6 7l4 3 4-3" stroke="#474747" fill="none"/></svg></div>
<div class="abs foot-contact" style="top:2071px">info@quenzmail.com</div>
<div class="abs foot-social" style="left:762px"></div>
<div class="abs foot-social" style="left:786px"></div>
<div class="abs foot-social" style="left:810px"></div>
<div class="abs copyright">© Copyright 2017 Test All Rights Reserved</div>
</body>
</html>
```